Salmon Shop that sells both wholesale and retail salmon in a variety of ways.

"Harbour Fillet Co" is a business that is selling atlantic salmon in every way possible. We will be a salmon butcher to the public for retail purchase and we will also be out and about trying to sell our products to restaurants cafes and any other wholesale way. Our product is from Tasmania but we will be trading on the Sunshine Coast. The shop design has an urban, rustic feel and very much about the product. One of the owners has worked on salmon farms for 15 years and we want it to be very specialised and quality. I have nothing to offer you to help with this design....I would like both a salmon on the card, not sure if image or silohette is best and would like the other side to have a fillet with a tag of some sort. We are looking for a logo also. Use a photo of an Atlantic Salmon, Atlantic Salmon have two fins along the back.
Updates

Project Deadline Extended Reason: I am extending the deadline as I have still not got exactly what I want. All designers have added something great to what I am after and I just need someone to pull it all together. I have put in a new brief with a sketched image to help so we can get this perfect. Please read all the instructions. Thank you Added Monday, February 16, 2015

Target Market(s)

Restaurants, cafes

Industry/Entity Type

Retail

Contact Information for Business Card

Harbour Fillet Co (Not to have "Shop" at the end.Shop 7/210-236 Brisbane RdMooloolaba 4557

Colors
1c66ab

Requirements
Must have
• logo for harbour fillet Co with the S being salmon fillet of fresh salmon on white platemap of tasmaniasepia /black and white image of atlantic salmon
Nice to have
• fillet of salmonmap of tasmaniasalmon
Should not have
• Not Shop at the end.

```html
<!DOCTYPE html>
<html lang="en">
<head>
<meta charset="utf-8">
<title>Harbour Fillet Co – Business Card</title>
<link rel="stylesheet" href="https://fonts.googleapis.com/css2?family=Montserrat:wght@500;600;700&family=Quicksand:wght@400;600&display=swap">
<style>
  :root {
    --backdrop: #e8e3da;
    --card: #fbfbfa;
    --card-edge: #e4e4e2;
    --band-dark: #5e4a2c;
    --band-light: #7b6543;
    --brand-ink: #ffffff;
    --name-blue: #3f93c9;
    --detail-grey: #a7a9ab;
    --icon-blue: #4a93c4;
    --web-ink: #1d1d1d;
    --fillet-deep: #ec6a2d;
    --fillet-light: #f7a37a;
    --herb-green: #7bb24a;
    --lemon: #f5c840;
    --silhouette: #262626;
  }
  * { box-sizing: border-box; margin: 0; padding: 0; }
  html, body { width: 1200px; height: 1000px; overflow: hidden; }
  body {
    background: var(--backdrop);
    position: relative;
    font-family: "Quicksand", sans-serif;
  }
  .card {
    position: absolute;
    left: 290px;
    width: 620px;
    height: 354px;
    background: var(--card);
    border: 1px solid var(--card-edge);
    border-radius: 4px;
    overflow: hidden;
    box-shadow: 0 10px 26px rgba(60, 45, 25, 0.22);
  }
  .card--front { top: 70px; }
  .card--back { top: 560px; }

  .brand-band {
    position: absolute;
    background: linear-gradient(180deg, var(--band-light), var(--band-dark));
    display: flex;
    align-items: center;
    z-index: 1;
  }
  .brand-name {
    font-family: "Montserrat", sans-serif;
    font-weight: 600;
    color: var(--brand-ink);
    text-transform: uppercase;
    letter-spacing: 0.02em;
    white-space: nowrap;
  }
  .brand-mark {
    border-radius: 50%;
    border: 3px solid var(--brand-ink);
    flex: none;
  }

  /* front */
  .card--front .brand-band {
    left: 0; top: 40px; width: 400px; height: 92px;
    padding-left: 22px; padding-right: 22px; gap: 14px;
  }
  .card--front .brand-mark { width: 42px; height: 42px; }
  .card--front .brand-name { font-size: 24px; }

  .product-photo {
    position: absolute;
    right: 0; top: 0;
    width: 300px; height: 165px;
    background:
      radial-gradient(ellipse 48% 40% at 30% 30%, var(--herb-green), transparent 70%),
      radial-gradient(ellipse 30% 30% at 12% 62%, var(--lemon), transparent 75%),
      radial-gradient(ellipse 60% 55% at 72% 62%, var(--fillet-deep), var(--fillet-light) 60%, transparent 80%),
      linear-gradient(180deg, #f3f0ec, var(--card));
  }

  .holder-name {
    position: absolute;
    left: 120px; top: 178px;
    font-size: 44px;
    font-weight: 600;
    line-height: 1.1;
    color: var(--name-blue);
  }
  .contact-list {
    position: absolute;
    left: 124px; top: 246px;
    list-style: none;
    color: var(--detail-grey);
    font-size: 18px;
    line-height: 30px;
  }
  .contact-list li { display: flex; align-items: center; gap: 10px; }
  .contact-icon { width: 14px; height: 14px; flex: none; }

  /* back */
  .card--back .brand-band {
    left: 0; top: 36px; width: 100%; height: 106px;
    justify-content: flex-end;
    padding-right: 34px; gap: 18px;
  }
  .card--back .brand-mark { width: 52px; height: 52px; }
  .card--back .brand-name { font-size: 32px; }

  .fish-silhouette {
    position: absolute;
    left: 170px; top: 180px;
    width: 300px; height: 92px;
    background: var(--silhouette);
    border-radius: 46px 30px 30px 46px;
  }
  .web-address {
    position: absolute;
    left: 0; right: 0; bottom: 26px;
    text-align: center;
    font-family: "Montserrat", sans-serif;
    font-weight: 700;
    font-size: 21px;
    color: var(--web-ink);
  }
</style>
</head>
<body>

<section class="card card--front" aria-label="Business card front">
  <div class="product-photo" role="img" aria-label="Photograph of a fresh salmon fillet with basil and lemon on a white plate"></div>
  <div class="brand-band">
    <span class="brand-mark" aria-hidden="true"></span>
    <span class="brand-name">Harbour Fillet Co</span>
  </div>
  <h1 class="holder-name">Sam Carter</h1>
  <ul class="contact-list">
    <li>
      <svg class="contact-icon" viewBox="0 0 14 14" aria-hidden="true"><rect x="2" y="2" width="10" height="10" fill="none" stroke="var(--icon-blue)" stroke-width="1.6"/></svg>
      555.204.8193
    </li>
    <li>
      <svg class="contact-icon" viewBox="0 0 14 14" aria-hidden="true"><path d="M3 1.5 L5.5 1.5 L6.5 4.5 L5 5.8 Q6.4 8.6 8.2 9 L9.5 7.5 L12.5 8.5 L12.5 11 Q12 12.5 10.5 12.5 Q2 12 1.5 3.5 Q1.5 2 3 1.5 Z" fill="var(--icon-blue)"/></svg>
      7/210-236
    </li>
    <li>
      <svg class="contact-icon" viewBox="0 0 14 14" aria-hidden="true"><path d="M7 13 Q2 7.5 2 5 A5 5 0 0 1 12 5 Q12 7.5 7 13 Z" fill="var(--icon-blue)"/><circle cx="7" cy="5" r="1.8" fill="var(--card)"/></svg>
      Wattlebay Rd Kirrawee 4812
    </li>
  </ul>
</section>

<section class="card card--back" aria-label="Business card back">
  <div class="brand-band">
    <span class="brand-mark" aria-hidden="true"></span>
    <span class="brand-name">Harbour Fillet Co</span>
  </div>
  <div class="fish-silhouette" role="img" aria-label="Black silhouette of an Atlantic salmon"></div>
  <p class="web-address">www.harbourfilletco.com.au</p>
</section>

</body>
</html>
```